Business Card Design Project

We're an orthopaedic office, and our colors are blue white and balck. Dealing with physicians and healthcare execs, I'd like this card to have a classy, yet overpowering wow factor.

Here are a couple of cards I like that are close to what I'm looking for:
http://www.pixelbazaro.com/design/392047
http://www.pixelbazaro.com/design/286390

Industry/Entity Type

Healthcare

```html
<!DOCTYPE html>
<html lang="en">
<head>
<meta charset="utf-8">
<title>Crestline Orthopaedic – Business Card</title>
<link href="https://fonts.googleapis.com/css2?family=Questrial&display=swap" rel="stylesheet">
<style>
  :root {
    --backdrop: #2b2b2d;
    --card-white: #f7f7f8;
    --brand-blue: #1a22b4;
    --brand-navy: #27318f;
    --gradient-top: #25309e;
    --gradient-bottom: #6b8fe6;
    --ink-light: #ffffff;
    --ink-soft: rgba(255,255,255,0.88);
  }
  * { margin: 0; padding: 0; box-sizing: border-box; }
  html, body {
    width: 1200px; height: 900px; overflow: hidden;
    background: var(--backdrop);
    font-family: "Questrial", sans-serif;
  }
  .sheet {
    width: 1200px; height: 900px;
    display: flex; flex-direction: column;
    align-items: center; justify-content: center; gap: 56px;
  }
  .card {
    width: 600px; height: 343px;
    border-radius: 4px;
    box-shadow: 0 18px 40px rgba(0,0,0,0.45);
    position: relative; overflow: hidden;
  }
  /* Front */
  .card-front {
    background: var(--card-white);
    display: flex; align-items: center; justify-content: center;
  }
  .brand-lockup { display: flex; align-items: center; gap: 20px; }
  .brand-dot {
    width: 64px; height: 64px; border-radius: 50%;
    background: var(--brand-blue); flex: none;
  }
  .brand-name {
    color: var(--brand-navy);
    font-size: 22px; line-height: 1.25; letter-spacing: 0.5px;
  }
  /* Back */
  .card-back {
    background: linear-gradient(160deg, var(--gradient-top) 0%, var(--gradient-bottom) 100%);
    color: var(--ink-light);
  }
  .holder { position: absolute; left: 190px; top: 38px; }
  .holder-name { font-size: 22px; letter-spacing: 0.3px; }
  .holder-title { font-size: 14px; margin: 4px 0 0 78px; color: var(--ink-soft); }
  .contact {
    position: absolute; left: 46px; top: 132px;
    list-style: none; font-size: 13px; line-height: 2; color: var(--ink-soft);
  }
  .contact .cell { margin-bottom: 14px; color: var(--ink-light); }
  .back-mark {
    position: absolute; right: 48px; bottom: 56px;
    display: flex; align-items: center; gap: 14px;
  }
  .back-mark .brand-dot { width: 72px; height: 72px; background: #0d18b0; }
  .back-mark .mark-name { font-size: 30px; color: #0d18b0; letter-spacing: 1px; }
</style>
</head>
<body>
<main class="sheet">
  <section class="card card-front" aria-label="Card front">
    <div class="brand-lockup">
      <span class="brand-dot"></span>
      <p class="brand-name">CRESTLINE<br>Orthopaedic &amp; Sports<br>Medicine Center</p>
    </div>
  </section>

  <section class="card card-back" aria-label="Card back">
    <div class="holder">
      <p class="holder-name">Declan Whitford</p>
      <p class="holder-title">CEO</p>
    </div>
    <ul class="contact">
      <li class="cell">Cell: (555) 274-0193</li>
      <li>1870 Harbor Ridge Dr, Fairmont, LA 70412</li>
      <li>dwhitford@crestlineortho.com</li>
    </ul>
    <div class="back-mark">
      <span class="brand-dot"></span>
      <span class="mark-name">CRESTLINE</span>
    </div>
  </section>
</main>
</body>
</html>
```